Help develop the "Tumble Beer" Logo & Can Design for new beer!

We're a new beer being produced in the Caribbean. Thus looking for a beer logo design that
1) capitalizes on the word "Tumble" for further beer lines that spin off of this first one. EXAMPLES OF OTHER BEER NAMES TO BE PRODUCED THAT HAVE TO HAVE TIE IN TO ORIGINAL DESIGN: "One Tumble Beer", "My Cousins Wabbaly Beer" "Pelkaroo Tumble Beer" "Lemme guess Tumble Beer" "Pass me a Tumble Beer", "Gorvela Tumble Beer" etc etc etc,

2) has unique visual impact,
3) Logo has to be usable across variety of mediums,
4) 4 color maximum,
5) Island art feel,
6) Tumble Beer needs to convey a since of "lightness and slight tongue-in-cheek or off beat humor"...but not overwhelming,
7) Each subsequent label names (see above) needs to be distinctly color coded, but connects to the overarching theme of the brand with distinctive interpretations of each beer’s name.
8) Needs to be BOLD in statement and color.

You can get inspiration from some of these logo's. Follow this link: http://www.quillmarkstudio.com/vintage-logos/
or http://www.shelfgallerydaily.com/2014/12/30-beers-for-30-years-2001-to-2006.html

Also see attached files for inspiration!!!

Reason: We've extended the deadline for this project! Thus submit any new designs sooner than later. Thanks!

Male: Wear jeans & baseball cap, Played H.S. sports, Hunts/fish/golfDrive a truck or SUV, Work a blue collar job, Like working in the garage or on the landLike football/basketball/baseball, Are married high school sweetheart and have childrenAre from southern states...or wished they were, Chews tobacco or smokeDrink beerFemale: Attended college/community collegeAre married with kidsRide motorcycles, 4x4, ATV’sDrive Trucks or vansFish/camp/garden/sewDo craftsDrink beerGets manicures/pedicuresWears jewelry & jeans

Tumble Beer

Emblem Logo
Pictorial/Combination Logo
Abstract Logo
Character Logo
Wordmark Logo
• Eye catching & readable shelf presentation. Non-Standard art. High definition. Bold Statement. Clear design elements, various color options, High color contrast (like attached files) are needed for visual impact. Simple elements that conveys essence of the brand.
• You are designing the whole "beer can" logo elements, not just the the main logo. Things like background and side panels. Back panel for ingredients and messages to be added to. This is an "overall" can design, not just a single logo design.
• MUST HAVE THESE WORDS/SENTENCES/SECTIONS:
• Sentences: Our Tumble ales and lagers are handcrafted with some of the best ingredients the Caribbean has to offer!
• Section: So, Why Do we use can's?
• Can's eliminate potential light damage, reduce the risk of oxidation are lighter and chill quicker. Can be enjoyed on beaches and make for great recycling and table art. Plus they are the most recycled and eco-friendly material we can use. Tumble!
• BREWED AND BOTTLED/PACKED BY:
• IMPORTED BY
• ALCOHOL (ALC) ______% BY VOLUME (VOL)
• Recyclable
• GOVERNMENT WARNING:
• (1) According to the Surgeon General, women should not drink alcoholic beverages during pregnancy because of the risk of birth defects. (2) Consumption of
• alcoholic beverages impairs your ability to drive a car or operate machinery, and may cause health problems.
• Description: (This will change from beer to beer but this is good example of type language we would be using. "This Tumble Beer has a pletheria of Island goodness (there are hints of passion fruit, mango, and pineapple) along with some pleasant bitterness IPAs are known for. We can honestly say these sweet and savory flavors pair perfectly with this beer and you'll get a kick out of the IPA notes too!"
• nudity, graphic language, skulls, flames,

```html
<!DOCTYPE html>
<html lang="en">
<head>
<meta charset="utf-8">
<title>Gorvela Tumble Beer — Logo &amp; Can Label</title>
<link rel="stylesheet" href="https://fonts.googleapis.com/css2?family=Fira+Sans+Condensed:wght@400;600;800&display=swap">
<style>
  :root{
    --paper:#ffffff;
    --ink:#222222;
    --band:#1c1c1e;
    --stage-light:#f1f1f3;
    --stage-dark:#c9cbd0;
    --navy:#1f3a5a;
    --navy-deep:#173049;
    --sky:#8ecbf0;
    --sky-soft:#5f93bd;
    --white:#ffffff;
  }
  *{margin:0;padding:0;box-sizing:border-box}
  html,body{width:1200px;height:2364px;overflow:hidden;background:var(--paper)}
  body{font-family:"Fira Sans Condensed",sans-serif;position:relative}

  .logo-sheet{position:absolute;left:0;top:0;width:1200px;height:962px;background:var(--paper);
    display:flex;align-items:center;justify-content:center}
  .wordmark{text-align:center;color:var(--ink);font-weight:800;line-height:.9;text-transform:uppercase}
  .wordmark .line-sm{display:block;font-size:52px;letter-spacing:6px}
  .wordmark .line-lg{display:block;font-size:170px;letter-spacing:4px}
  .wordmark .line-md{display:block;font-size:78px;letter-spacing:22px}

  .dark-band{position:absolute;left:0;top:962px;width:1200px;height:164px;background:var(--band);
    display:flex;align-items:center;justify-content:center}
  .dark-band .wordmark{color:var(--white)}
  .dark-band .line-sm{font-size:18px;letter-spacing:3px}
  .dark-band .line-lg{font-size:56px;letter-spacing:2px}
  .dark-band .line-md{font-size:26px;letter-spacing:8px}

  .can-stage{position:absolute;left:0;top:1126px;width:1200px;height:648px;
    background:radial-gradient(ellipse at center,var(--stage-light) 0%,var(--stage-dark) 100%)}

  .can-label{position:absolute;left:0;top:1774px;width:1200px;height:590px;background:var(--navy);color:var(--sky)}

  .panel-back{position:absolute;left:0;top:0;width:430px;height:590px}
  .warning{position:absolute;left:14px;top:30px;width:520px;height:80px;transform-origin:0 0;
    transform:translate(0,520px) rotate(-90deg);color:var(--white);font-size:12.5px;line-height:1.35;opacity:.85}
  .compass{position:absolute;left:238px;top:34px}
  .tagline{position:absolute;left:118px;top:150px;width:295px;font-size:31px;font-weight:600;line-height:1.18;
    text-align:justify;text-align-last:left}
  .packer{position:absolute;left:206px;top:398px;color:var(--white);font-size:13px;line-height:1.35;letter-spacing:.5px}
  .packer-icon{position:absolute;left:160px;top:400px}
  .crest{position:absolute;left:236px;top:500px;width:62px;height:46px;background:var(--white);opacity:.85;border-radius:4px}

  .panel-front{position:absolute;left:438px;top:0;width:430px;height:590px;background:var(--navy-deep);overflow:hidden}
  .pattern{position:absolute;top:0;height:590px;width:140px;
    background:linear-gradient(180deg,var(--sky-soft),var(--navy) 50%,var(--sky-soft))}
  .pattern.left{left:0}
  .pattern.right{right:0}
  .front-name{position:absolute;left:50%;top:50%;transform:translate(-50%,-50%) rotate(90deg);
    color:var(--sky);font-weight:800;text-transform:uppercase;text-align:center;line-height:.88;white-space:nowrap}
  .front-name .line-sm{display:block;font-size:46px;letter-spacing:6px}
  .front-name .line-lg{display:block;font-size:150px;letter-spacing:4px}
  .front-name .line-md{display:block;font-size:70px;letter-spacing:20px}

  .panel-side{position:absolute;left:868px;top:0;width:332px;height:590px}
  .recycle{position:absolute;left:138px;top:56px}
  .side-heading{position:absolute;left:20px;top:160px;color:var(--white);font-size:20px;font-weight:800;letter-spacing:.5px}
  .side-copy{position:absolute;left:20px;top:206px;width:292px;font-size:17.5px;font-weight:600;line-height:1.28;
    text-align:justify}
  .abv{position:absolute;left:44px;top:420px;color:var(--white);font-size:11.5px;line-height:1.5;letter-spacing:.5px}
  .flourish{position:absolute;left:130px;top:492px;width:70px;height:18px;background:var(--white);opacity:.8;border-radius:9px}
</style>
</head>
<body>

<section class="logo-sheet">
  <h1 class="wordmark">
    <span class="line-sm">Gorvela</span>
    <span class="line-lg">Tumble</span>
    <span class="line-md">Beer</span>
  </h1>
</section>

<section class="dark-band">
  <div class="wordmark">
    <span class="line-sm">Gorvela</span>
    <span class="line-lg">Tumble</span>
    <span class="line-md">Beer</span>
  </div>
</section>

<section class="can-stage" role="img" aria-label="Three beer cans showing the back, front and side panels of the label"></section>

<section class="can-label">
  <div class="panel-back">
    <p class="warning">GOVERNMENT WARNING: (1) According to the Surgeon General, women should not drink alcoholic beverages during pregnancy because of the risk of birth defects. (2) Consumption of alcoholic beverages impairs your ability to drive a car or operate machinery, and may cause health problems.</p>
    <svg class="compass" width="70" height="70" viewBox="0 0 70 70" aria-hidden="true">
      <circle cx="35" cy="35" r="22" fill="none" stroke="#ffffff" stroke-width="3"/>
      <path d="M35 2 L40 35 L35 68 L30 35 Z M2 35 L35 30 L68 35 L35 40 Z" fill="#ffffff"/>
    </svg>
    <p class="tagline">Our Tumble ales and lagers are handcrafted with some of the best ingredients the Caribbean has to offer!</p>
    <svg class="packer-icon" width="34" height="34" viewBox="0 0 34 34" aria-hidden="true">
      <circle cx="17" cy="17" r="12" fill="none" stroke="#ffffff" stroke-width="3"/>
      <circle cx="17" cy="17" r="3" fill="#ffffff"/>
    </svg>
    <p class="packer">BREWED AND BOTTLED/PACKED BY:<br>IMPORTED BY</p>
    <div class="crest" role="img" aria-label="Crossed pistols emblem"></div>
  </div>

  <div class="panel-front">
    <div class="pattern left" role="img" aria-label="Light blue island paisley pattern"></div>
    <div class="pattern right" role="img" aria-label="Light blue island paisley pattern"></div>
    <div class="front-name">
      <span class="line-sm">Gorvela</span>
      <span class="line-lg">Tumble</span>
      <span class="line-md">Beer</span>
    </div>
  </div>

  <div class="panel-side">
    <svg class="recycle" width="56" height="56" viewBox="0 0 56 56" aria-hidden="true">
      <circle cx="28" cy="28" r="25" fill="none" stroke="#ffffff" stroke-width="3"/>
      <path d="M28 12 L40 34 H16 Z" fill="none" stroke="#ffffff" stroke-width="3" stroke-linejoin="round"/>
    </svg>
    <h2 class="side-heading">SO, WHY DO WE USE CAN'S?</h2>
    <p class="side-copy">Can's eliminate potential light damage, reduce the risk of oxidation are lighter and chill quicker. Can be enjoyed on beaches and make for great recycling and table art. Plus they are the most recycled and eco-friendly material we can use. Tumble!</p>
    <p class="abv">ALCOHOL (ALC) ______% BY VOLUME (VOL)<br>Recyclable</p>
    <div class="flourish" role="img" aria-label="Small wave flourish ornament"></div>
  </div>
</section>

</body>
</html>
```